Business cards for Norwegian software consultancy business

We are in need of business cards for our Norwegian consultancy company.
“Vilma Tronsoft AS” specializes in software development, architecture and agile methodology, providing mostly on-site services at customers.
The cards should reflect a certain level of business professionalism with an elegant touch, while paying tribute to our modern and technological heritage. Our logo should be featured, as well as room for basic information about the cardholder and legal information of the company (company name, address and VAT number).
We would like our cards to reflect that we are a modern consulting company. It should present a professional image that people will remember. The texture and color pallette should reflect our professionalism and reliability, so we prefer a light color pallette with colors such as gray, white, blue and black. The number of colors used should however not be overwhelming, with the text being distinct and readable.
We are open to untraditional layouts and playful designs as long as they communicate the intent stated above.
You could also take a look at our website http://www.tronsoft-demo.no for input on our visual profile.
Our logo is attached in the form of vectors and rasterized PNG. Please comment if you would like the black-white and/or inverted versions as well.
Architecture
Company information:
Vilma Tronsoft AS
Lindåsgata 7, 3129 Nøtterøy
481 62 509
info@tronsoft-demo.no
www.tronsoft-demo.no
Employee information:
Full name
Title
Email
Phone

```html
<!DOCTYPE html>
<html lang="no">
<head>
<meta charset="utf-8">
<title>Vilma Tronsoft AS – Business Card</title>
<link rel="stylesheet" href="https://fonts.googleapis.com/css2?family=Lato:wght@400;700&display=swap">
<style>
  :root {
    --backdrop: #d9d9d9;
    --card: #ffffff;
    --ink: #2b2b2b;
    --ink-soft: #4a4a4a;
    --blue: #4f8fc6;
    --rule: #bfbfbf;
  }
  * { box-sizing: border-box; margin: 0; padding: 0; }
  html, body {
    width: 1200px; height: 900px; overflow: hidden;
    background: var(--backdrop);
    font-family: "Lato", sans-serif;
    color: var(--ink);
  }
  .card {
    position: absolute; left: 150px; top: 170px;
    width: 900px; height: 560px;
    background: var(--card);
    box-shadow: 0 10px 30px rgba(0,0,0,0.18);
    overflow: hidden;
  }
  .brand-panel {
    position: absolute; left: 0; top: 0; width: 420px; height: 100%;
    border-right: 1px solid var(--rule);
  }
  .logo {
    position: absolute; left: 60px; top: 230px;
    display: flex; align-items: center; gap: 16px;
  }
  .logo-square { width: 34px; height: 34px; background: var(--blue); }
  .logo-name {
    font-size: 40px; font-weight: 400; color: var(--ink-soft);
    letter-spacing: 1px;
  }
  .website {
    position: absolute; left: 60px; bottom: 70px;
    font-size: 20px; letter-spacing: 5px; color: var(--ink);
  }
  .info-panel { position: absolute; left: 475px; top: 70px; }
  .holder-name { font-size: 34px; color: var(--blue); font-weight: 400; }
  .holder-title { font-size: 19px; text-transform: uppercase; margin-top: 2px; letter-spacing: 0.5px; }
  .company { margin-top: 36px; font-size: 23px; line-height: 1.3; font-style: normal; }
  .company-name { font-weight: 700; }
  .contacts { margin-top: 36px; list-style: none; font-size: 23px; line-height: 1.3; }
  .contacts li { display: flex; align-items: center; gap: 14px; }
  .contacts svg { width: 20px; height: 20px; flex: none; }
  .corner-accent {
    position: absolute; right: 0; bottom: 0;
    width: 96px; height: 20px;
    background: var(--blue);
  }
</style>
</head>
<body>
  <article class="card">
    <section class="brand-panel">
      <div class="logo">
        <span class="logo-square"></span>
        <span class="logo-name">Vilma Tronsoft</span>
      </div>
      <p class="website">www.tronsoft-demo.no</p>
    </section>

    <section class="info-panel">
      <h1 class="holder-name">Kari Nordvik</h1>
      <p class="holder-title">Director</p>
      <address class="company">
        <div class="company-name">Vilma Tronsoft AS</div>
        <div>Lindåsgata 7</div>
        <div>3129 Nøtterøy</div>
      </address>
      <ul class="contacts">
        <li>
          <svg viewBox="0 0 20 20" aria-hidden="true"><path d="M5 2l3 4-2 2c1 2 3 4 5 5l2-2 4 3-2 3C9 17 3 11 2 4z" fill="none" stroke="var(--blue)" stroke-width="1.6"/></svg>
          481 62 509
        </li>
        <li>
          <svg viewBox="0 0 20 20" aria-hidden="true"><rect x="5" y="2" width="10" height="6" fill="none" stroke="var(--blue)" stroke-width="1.6"/><rect x="2" y="8" width="16" height="8" fill="var(--blue)"/></svg>
          481 62 510
        </li>
        <li>
          <svg viewBox="0 0 20 20" aria-hidden="true"><rect x="2" y="4" width="16" height="12" fill="none" stroke="var(--blue)" stroke-width="1.6"/><path d="M2 4l8 7 8-7" fill="none" stroke="var(--blue)" stroke-width="1.6"/></svg>
          knordvik@tronsoft-demo.no
        </li>
      </ul>
    </section>

    <div class="corner-accent" role="img" aria-label="Decorative corner accent in brand blue"></div>
  </article>
</body>
</html>
```